International Trading Company, 'KIRO' needs a Business Card

The company name is "KIRO" and it has own logo design.
I'd like to use its logo on this business card.
I need two side Business Card.
I'll look forward to your great design.
Thank you very much in advance.

Contact Information for Business Card

Company Name : Kiro Harbour Limited
Information Example
Dorian Pallister
Mobile(use icon please) : 1 (212) 555-0143
Tel(use icon please) : 1 (212) 555-0178
Email(use icon please) : dorian27@kiroharbour-mail.com
Address(use icon please) : 482 Halden Ave, New York, NY 10160, USA

```html
<!DOCTYPE html>
<html lang="en">
<head>
<meta charset="utf-8">
<title>Kiro Harbour Limited — Business Card</title>
<link rel="stylesheet" href="https://fonts.googleapis.com/css2?family=Lato:ital,wght@0,400;0,700;0,900;1,400&display=swap">
<style>
  :root {
    --canvas-bg: #e9e9ea;
    --card-white: #ffffff;
    --card-dark-top: #3b3b3c;
    --card-dark-bottom: #161617;
    --logo-grey: #5a5a5c;
    --logo-on-dark: #77777a;
    --text-dark: #1f1f21;
    --text-mid: #4a4a4d;
    --rule: #8d8d90;
    --shadow: rgba(0, 0, 0, 0.18);
  }
  * { box-sizing: border-box; margin: 0; padding: 0; }
  html, body {
    width: 1200px;
    height: 1050px;
    overflow: hidden;
    background: var(--canvas-bg);
    font-family: "Lato", Arial, sans-serif;
  }
  .canvas {
    width: 1200px;
    height: 1050px;
    display: flex;
    flex-direction: column;
    align-items: center;
    justify-content: center;
    gap: 56px;
  }
  .card {
    width: 760px;
    height: 434px;
    position: relative;
    box-shadow: 0 10px 28px var(--shadow);
  }
  /* Front */
  .card-front { background: var(--card-white); }
  .front-wordmark {
    position: absolute;
    left: 64px;
    top: 44px;
    font-weight: 900;
    font-size: 112px;
    letter-spacing: 6px;
    line-height: 1;
    color: var(--logo-grey);
  }
  .front-rule {
    position: absolute;
    left: 150px;
    right: 56px;
    top: 190px;
    height: 1px;
    background: var(--rule);
  }
  .contact-list {
    position: absolute;
    left: 64px;
    top: 208px;
    list-style: none;
  }
  .contact-item {
    display: flex;
    align-items: center;
    gap: 12px;
    font-size: 17px;
    line-height: 26px;
    color: var(--text-dark);
  }
  .contact-icon { width: 14px; height: 14px; fill: var(--text-mid); flex: none; }
  .holder {
    position: absolute;
    right: 56px;
    top: 276px;
    text-align: right;
  }
  .holder-name {
    font-size: 28px;
    font-style: italic;
    color: var(--text-mid);
    padding-bottom: 8px;
  }
  .holder-rule {
    position: absolute;
    right: 56px;
    top: 326px;
    width: 220px;
    height: 1px;
    background: var(--rule);
  }
  .address {
    position: absolute;
    right: 56px;
    top: 342px;
    text-align: right;
    font-size: 17px;
    line-height: 24px;
    color: var(--text-dark);
  }
  .address-line { display: flex; align-items: center; justify-content: flex-end; gap: 8px; }
  /* Back */
  .card-back {
    background: linear-gradient(160deg, var(--card-dark-top) 0%, var(--card-dark-bottom) 100%);
    display: flex;
    align-items: center;
    justify-content: center;
  }
  .back-wordmark {
    font-weight: 900;
    font-size: 190px;
    letter-spacing: 10px;
    line-height: 1;
    color: var(--logo-on-dark);
  }
</style>
</head>
<body>
<main class="canvas">
  <section class="card card-front" aria-label="Business card front">
    <div class="front-wordmark">KIRO</div>
    <div class="front-rule"></div>
    <ul class="contact-list">
      <li class="contact-item">
        <svg class="contact-icon" viewBox="0 0 14 14" aria-hidden="true"><rect x="3.5" y="0.5" width="7" height="13" rx="1.5" fill="none" stroke="currentColor" style="stroke:var(--text-mid)"/><rect x="5" y="2" width="4" height="8"/><circle cx="7" cy="11.8" r="0.8"/></svg>
        <span>1 (212) 555-0143</span>
      </li>
      <li class="contact-item">
        <svg class="contact-icon" viewBox="0 0 14 14" aria-hidden="true"><path d="M3 1l2.5 0 1 3.2-1.5 1.2c.8 1.6 2 2.8 3.6 3.6l1.2-1.5 3.2 1v2.5c0 .6-.5 1-1 1C6.3 13 1 7.7 1 2c0-.5.4-1 1-1z"/></svg>
        <span>1 (212) 555-0178</span>
      </li>
      <li class="contact-item">
        <svg class="contact-icon" viewBox="0 0 14 14" aria-hidden="true"><path d="M1 3h12v8H1z M1.5 3.5L7 8l5.5-4.5" style="fill:var(--text-mid)"/><path d="M1.5 3.6L7 7.8l5.5-4.2" fill="none" stroke="#fff" stroke-width="1"/></svg>
        <span>dorian27@kiroharbour-mail.com</span>
      </li>
      <li class="contact-item">
        <svg class="contact-icon" viewBox="0 0 14 14" aria-hidden="true"><circle cx="7" cy="7" r="6"/><path d="M1 7h12M7 1c-2.2 2-2.2 10 0 12M7 1c2.2 2 2.2 10 0 12" fill="none" stroke="#fff" stroke-width="0.9"/></svg>
        <span>www.kiroharbour-web.com</span>
      </li>
    </ul>
    <div class="holder"><p class="holder-name">Dorian Pallister</p></div>
    <div class="holder-rule"></div>
    <div class="address">
      <p class="address-line">
        <svg class="contact-icon" viewBox="0 0 14 14" aria-hidden="true"><path d="M7 1.5L1 7h2v5.5h3.2V9h1.6v3.5H11V7h2z"/></svg>
        <span>482 Halden Ave</span>
      </p>
      <p>New York, NY 10160, USA</p>
    </div>
  </section>

  <section class="card card-back" aria-label="Business card back">
    <div class="back-wordmark">KIRO</div>
  </section>
</main>
</body>
</html>
```